The Timber Loft

We need a business card design for our wardrobe company.
Please visit our website www.zorvelcabinets.com to get an idea of who we are.

```html
<!DOCTYPE html>
<html lang="en">
<head>
<meta charset="UTF-8">
<title>The Timber Loft – Business Card</title>
<link rel="stylesheet" href="https://fonts.googleapis.com/css2?family=Lato:wght@400;700&display=swap">
<style>
  :root {
    --backdrop: #6e4421;
    --card: #111111;
    --ink: #f2f2f2;
    --rule: #8a8a8a;
  }
  * { margin: 0; padding: 0; box-sizing: border-box; }
  html, body {
    width: 1200px;
    height: 900px;
    overflow: hidden;
  }
  body {
    position: relative;
    background: var(--backdrop);
    font-family: "Lato", Arial, sans-serif;
    color: var(--ink);
  }
  .card {
    position: absolute;
    background: var(--card);
  }
  .card--front { left: 330px; top: 90px; width: 555px; height: 345px; }
  .card--back  { left: 330px; top: 470px; width: 560px; height: 343px; }

  .front-content {
    position: absolute;
    left: 0; right: 0;
    top: 65px;
    text-align: center;
  }
  .person-name {
    font-weight: 700;
    font-size: 22px;
    letter-spacing: 0.5px;
    line-height: 26px;
  }
  .person-title {
    font-size: 16px;
    line-height: 20px;
  }
  .icon-row {
    display: flex;
    align-items: center;
    justify-content: center;
    margin: 12px auto 8px;
    width: 180px;
    gap: 4px;
  }
  .icon-row .rule {
    flex: 1;
    height: 1px;
    background: var(--rule);
  }
  .icon-row svg { display: block; }
  .contact-list,
  .address {
    font-size: 16px;
    line-height: 20px;
  }
  .divider {
    width: 186px;
    height: 1px;
    background: var(--rule);
    margin: 11px auto 10px;
  }

  .brand {
    position: absolute;
    left: 100px;
    top: 142px;
    display: flex;
    align-items: center;
    gap: 20px;
  }
  .brand-mark {
    width: 60px;
    height: 60px;
    border: 2px solid var(--ink);
  }
  .brand-text {
    text-align: center;
  }
  .brand-name {
    font-weight: 700;
    font-size: 18px;
    line-height: 24px;
    text-transform: uppercase;
    letter-spacing: 0.3px;
  }
  .brand-tagline {
    font-size: 16px;
    line-height: 22px;
  }
</style>
</head>
<body>

<section class="card card--front">
  <div class="front-content">
    <div class="person-name">MARCUS HALE</div>
    <div class="person-title">Managing Director</div>

    <div class="icon-row">
      <span class="rule"></span>
      <svg width="24" height="24" viewBox="0 0 24 24" aria-label="Phone">
        <circle cx="12" cy="12" r="11" fill="var(--ink)"/>
        <path d="M6 10 Q12 5 18 10 L16 12 L14 10 L10 10 L8 12 Z" fill="#111"/>
        <rect x="8" y="12" width="8" height="5" rx="1" fill="#111"/>
      </svg>
      <svg width="24" height="24" viewBox="0 0 24 24" aria-label="Email">
        <circle cx="12" cy="12" r="11" fill="var(--ink)"/>
        <rect x="6" y="8" width="12" height="8" fill="none" stroke="#111" stroke-width="1.5"/>
        <path d="M6 8 L12 13 L18 8" fill="none" stroke="#111" stroke-width="1.5"/>
      </svg>
      <svg width="24" height="24" viewBox="0 0 24 24" aria-label="Website">
        <circle cx="12" cy="12" r="11" fill="var(--ink)"/>
        <circle cx="12" cy="12" r="6" fill="none" stroke="#111" stroke-width="1.5"/>
        <path d="M6 12 H18 M12 6 Q8 12 12 18 M12 6 Q16 12 12 18" fill="none" stroke="#111" stroke-width="1.2"/>
      </svg>
      <span class="rule"></span>
    </div>

    <div class="contact-list">
      <div class="contact-phone">0207 555 0148</div>
      <div class="contact-email">info@zorvelcabinets.com</div>
      <div class="contact-web">www.zorvelcabinets.com</div>
    </div>

    <div class="divider"></div>

    <div class="address">
      <div>Alder Court, 42 Mill Lane</div>
      <div>London N4 7QT</div>
    </div>
  </div>
</section>

<section class="card card--back">
  <div class="brand">
    <span class="brand-mark"></span>
    <div class="brand-text">
      <div class="brand-name">The Timber Loft</div>
      <div class="brand-tagline">Built Square, Built True</div>
    </div>
  </div>
</section>

</body>
</html>
```